Web Design Business Card

I need a new business card designed, we recently rebranded and I need to get a fresh design to match our new logo, colours and branding.

Details:

Dorian Keeble | Founder & CEO
Address: 7 Fernhollow Lane, #04-09 Maplecrest Vale, Singapore 583104
Tel: +65 93468120
Web: www.plumtrove.com.sg
hello@plumtrove.com.sg

I've attached my old card as well

Requirements
Must have
• Front and Back
Interesting use of logo
Correct use of colour scheme

```html
<!DOCTYPE html>
<html lang="en">
<head>
<meta charset="utf-8">
<title>Plumtrove Business Card</title>
<link rel="stylesheet" href="https://fonts.googleapis.com/css2?family=Barlow:wght@400;500;700&family=Barlow+Semi+Condensed:wght@500&display=swap">
<style>
  :root {
    --stage: #262626;
    --card-white: #efefef;
    --brand-blue: #2fa6dc;
    --brand-sky: #5cc3ef;
    --brand-taupe: #8a7466;
    --ink: #4a4a4a;
    --violet: #5a2e9a;
    --indigo: #3d3f9e;
    --periwinkle: #5f7fc4;
    --orchid: #a05bb8;
  }
  * { box-sizing: border-box; margin: 0; padding: 0; }
  html, body { width: 1200px; height: 900px; overflow: hidden; }
  body {
    background: var(--stage);
    font-family: "Barlow", Arial, sans-serif;
    display: flex;
    align-items: center;
    justify-content: center;
    gap: 40px;
  }
  .card {
    position: relative;
    width: 540px;
    height: 310px;
    overflow: hidden;
    box-shadow: 0 10px 30px rgba(0,0,0,0.5);
  }
  .facet-field {
    position: absolute;
    inset: 0;
    background:
      linear-gradient(160deg, rgba(160,91,184,0.85) 0%, rgba(160,91,184,0) 45%),
      linear-gradient(120deg, var(--violet) 0%, var(--indigo) 50%, var(--periwinkle) 100%);
  }
  /* Front */
  .card-front .brand {
    position: absolute;
    left: 70px;
    top: 105px;
    display: flex;
    align-items: center;
    gap: 16px;
  }
  .brand-dot {
    border-radius: 50%;
    background: var(--brand-sky);
    flex: none;
  }
  .card-front .brand-dot { width: 70px; height: 70px; }
  .brand-name {
    font-weight: 700;
    color: var(--brand-taupe);
    line-height: 1;
    letter-spacing: 0.5px;
  }
  .card-front .brand-name { font-size: 56px; }
  .brand-tagline {
    font-weight: 700;
    color: var(--brand-sky);
    text-transform: uppercase;
    letter-spacing: 1px;
  }
  .card-front .brand-tagline { font-size: 14px; margin-top: 4px; }
  /* Back */
  .card-back { background: var(--card-white); }
  .card-back .facet-field { top: auto; height: 62px; }
  .name-tag {
    position: absolute;
    left: 0;
    top: 36px;
    width: 250px;
    height: 34px;
    background: var(--brand-blue);
    border-radius: 0 6px 6px 0;
    color: #fff;
    font-family: "Barlow Semi Condensed", Arial, sans-serif;
    font-weight: 500;
    font-size: 25px;
    line-height: 34px;
    padding-left: 96px;
    letter-spacing: 0.5px;
  }
  .role {
    position: absolute;
    left: 96px;
    top: 74px;
    font-size: 10px;
    color: var(--ink);
  }
  .address {
    position: absolute;
    left: 70px;
    top: 120px;
    font-size: 13px;
    line-height: 19px;
    color: var(--ink);
    font-style: normal;
  }
  .card-back .brand {
    position: absolute;
    left: 300px;
    top: 100px;
    display: flex;
    align-items: center;
    gap: 10px;
  }
  .card-back .brand-dot { width: 44px; height: 44px; }
  .card-back .brand-name { font-size: 34px; }
  .card-back .brand-tagline { font-size: 9px; margin-top: 2px; }
  .contacts {
    position: absolute;
    left: 210px;
    top: 170px;
    list-style: none;
    font-size: 13px;
    line-height: 19px;
    color: var(--ink);
  }
  .contacts .label { color: var(--brand-blue); }
</style>
</head>
<body>
  <section class="card card-front" aria-label="Card front">
    <div class="facet-field" role="img" aria-label="Faceted low-poly pattern in purple and blue tones"></div>
    <div class="brand">
      <span class="brand-dot"></span>
      <div>
        <div class="brand-name">plumtrove</div>
        <div class="brand-tagline">Web Design &amp; Consultancy</div>
      </div>
    </div>
  </section>

  <section class="card card-back" aria-label="Card back">
    <div class="name-tag">Dorian Keeble</div>
    <div class="role">Founder &amp; CEO</div>
    <address class="address">
      7 Fernhollow Lane,<br>
      #04-09 Maplecrest Vale,<br>
      Singapore 583104
    </address>
    <div class="brand">
      <span class="brand-dot"></span>
      <div>
        <div class="brand-name">plumtrove</div>
        <div class="brand-tagline">Web Design &amp; Consultancy</div>
      </div>
    </div>
    <ul class="contacts">
      <li><span class="label">T:</span> +65 93468120</li>
      <li><span class="label">E:</span> hello@plumtrove.com.sg</li>
      <li><span class="label">W:</span> www.plumtrove.com.sg</li>
    </ul>
    <div class="facet-field" role="img" aria-label="Faceted low-poly band in purple and blue tones"></div>
  </section>
</body>
</html>
```